Reminder card

We are an alternative health clinic. This project is for a postcard. The postcard is sent to our clients to remind them they have not been in the clinic for a long time and it's time for them to make an appointment. Our website is MendwellHaven.com
Updates

Project Deadline Extended
Reason: Extending deadline, thanks.

Target Market(s)

Our clients are usually adults between the ages of 35 - 55, 70% women, 30% men. These are educated, wealthy, people who are committed to their health. Our clients expect us to be professional and an authority in our field, but friendly, playful and open.

Industry/Entity Type

Health

Font styles to use
Other font styles liked:
• our name is blackjack and the rest of the website is open sans

Requirements
Must have
• The front of the postcard must have our logo and name (see attached).

The front of the post card must have this text:
Feel good and want to stay that way? Need a boost? It's time for your tune-up appointment at Mendwell Haven.

The right side on the back of the card must be blank for an address and stamp.

The left side on the back of the card must have our phone number (415.927.4413) and website (MendwellHaven.com).
Nice to have
• We have an egg theme in our office. Our website is MendwellHaven.com and if you look at it, you'll see the pictures of them.

The postcard should be in the same style as the website in color and tone.
Should not have
• We want things to be playful, but not look like something for children.

```html
<!DOCTYPE html>
<html lang="en">
<head>
<meta charset="utf-8">
<title>Mendwell Haven – Reminder Card</title>
<link rel="stylesheet" href="https://fonts.googleapis.com/css2?family=Dancing+Script:wght@500&family=Open+Sans:wght@400;600;700&display=swap">
<style>
  :root {
    --board-light: #fbfbfa;
    --board-mid: #eeeeec;
    --frame: #d9d9d6;
    --ink-dark: #1f1f1f;
    --ink-heading: #3e3e3e;
    --ink-soft: #555555;
    --sprout-green: #8fc24a;
    --sprout-pale: #e9f1dc;
    --shell-peach: #e7a57a;
    --shell-light: #f3cfb3;
  }
  * { margin: 0; padding: 0; box-sizing: border-box; }
  html, body {
    width: 741px;
    height: 1200px;
    overflow: hidden;
    background: var(--board-light);
  }
  .card {
    position: relative;
    width: 741px;
    height: 1200px;
    background: linear-gradient(180deg, var(--board-light) 0%, var(--board-mid) 55%, var(--board-light) 100%);
    border: 2px solid var(--frame);
    font-family: "Open Sans", sans-serif;
    text-align: center;
  }
  .brand-name {
    position: absolute;
    top: 30px;
    left: 0;
    width: 100%;
    font-family: "Dancing Script", cursive;
    font-weight: 500;
    font-size: 84px;
    line-height: 1.1;
    color: var(--ink-dark);
  }
  .prompt {
    position: absolute;
    top: 220px;
    left: 0;
    width: 100%;
    font-weight: 700;
    font-size: 26px;
    line-height: 37px;
    color: var(--ink-heading);
    text-transform: uppercase;
  }
  .boost {
    position: absolute;
    top: 316px;
    left: 0;
    width: 100%;
    font-weight: 600;
    font-size: 33px;
    color: var(--ink-soft);
  }
  .sprout-egg {
    position: absolute;
    top: 430px;
    left: 215px;
    width: 356px;
    height: 695px;
    border-radius: 40% 40% 48% 48% / 30% 30% 20% 20%;
    background: linear-gradient(180deg, var(--sprout-pale) 0%, var(--sprout-green) 22%, var(--sprout-pale) 50%, var(--shell-light) 62%, var(--shell-peach) 100%);
  }
  .reminder {
    position: absolute;
    top: 945px;
    left: 110px;
    width: 521px;
    font-weight: 400;
    font-size: 33px;
    line-height: 43px;
    color: var(--ink-dark);
  }
</style>
</head>
<body>
  <main class="card">
    <h1 class="brand-name">Mendwell Haven</h1>
    <p class="prompt">Feel good and want to stay<br>that way ?</p>
    <p class="boost">Need a boost ?</p>
    <div class="sprout-egg" role="img" aria-label="A young green sprout growing out of a cracked brown eggshell"></div>
    <p class="reminder">It’s time for your tune-up appointment at Mendwell Haven.</p>
  </main>
</body>
</html>
```